School Learner profile graphic representation

I have a set of ideas around communicating our school 'learner profile'. These represent the attitudes, habits and dispositions we are trying to develop through our curriculum and wider enrichment programme. I want the links between the ideas and concepts to be represented in some form of an inforgraphic which can be published and displayed for the whole community to connect with. we run two schools and want the profile to represent for both.

Target Market(s)

Students, Parents, Teachers, Wider community in education

Industry/Entity Type

Education

Font styles to use
Other font styles liked:
• Johnson p22

Colors

Designer to choose colors to be used in the design.

Requirements
Must have
• See my diagram in the ppt.
• The statements Aspiration, Agency, Agility, Altitude with the supporting descriptions. Ideally the values in the center is also represented. The two school logos should also be present somehow (both emblems at least). Let me know if the full logo files are required
Nice to have
• the numbering shown in my diagram is not absolutely necessary is it is not necessarily a linear process and rather cyclical and cross reinforcing

```html
<!DOCTYPE html>
<html lang="en">
<head>
<meta charset="utf-8">
<title>Envisioning Our Learners</title>
<link rel="stylesheet" href="https://fonts.googleapis.com/css2?family=Lexend:wght@400;500;600;700&family=Montserrat:wght@400;600&display=swap">
<style>
  :root {
    --red: #ee1c25;
    --red-deep: #c1161d;
    --ink: #2b2b2b;
    --grey-disc: #f0f0f0;
    --pattern: #ececec;
    --paper: #ffffff;
    --sky: #2f8fd6;
    --teal: #2bb3c0;
  }
  html, body {
    margin: 0;
    padding: 0;
    width: 848px;
    height: 1200px;
    overflow: hidden;
    background: var(--paper);
  }
  .poster { display: block; width: 848px; height: 1200px; }
  .title { font-family: "Lexend", sans-serif; font-weight: 600; fill: var(--red); }
  .label-lead { font-family: "Lexend", sans-serif; font-weight: 500; font-size: 11px; fill: var(--red-deep); }
  .label-key { font-family: "Lexend", sans-serif; font-weight: 500; font-size: 21px; fill: var(--red); }
  .label-desc { font-family: "Lexend", sans-serif; font-weight: 500; font-size: 14px; fill: var(--ink); }
  .school-name { font-family: "Lexend", sans-serif; font-weight: 700; font-size: 23px; fill: var(--ink); }
  .school-tag { font-family: "Montserrat", sans-serif; font-weight: 400; font-size: 15px; fill: var(--ink); }
  .school-name-alt { font-family: "Lexend", sans-serif; font-weight: 500; fill: var(--red-deep); }
  .pill { fill: var(--paper); stroke: var(--red-deep); stroke-width: 2; }
  .chain { fill: none; stroke: var(--red-deep); stroke-width: 34; }
  .node-ring { fill: var(--red-deep); }
  .node-disc { fill: var(--grey-disc); stroke: var(--paper); stroke-width: 3; }
  .flow-arrow { fill: none; stroke: var(--paper); stroke-width: 2; }
</style>
</head>
<body>
<svg class="poster" viewBox="0 0 1000 1415" xmlns="http://www.w3.org/2000/svg">
  <!-- background motif area -->
  <path role="img" aria-label="Faint geometric star pattern background" fill="var(--pattern)" opacity="0.5"
        d="M470 1415 L360 1230 L470 1040 L620 830 L920 830 L1000 900 L1000 1415 Z"/>

  <!-- frame -->
  <rect x="30" y="36" width="942" height="1344" fill="none" stroke="var(--red-deep)" stroke-width="7"/>

  <!-- title -->
  <text class="title" x="188" y="215" font-size="98" textLength="640" lengthAdjust="spacingAndGlyphs">ENVISIONING</text>
  <text class="title" x="194" y="306" font-size="48" textLength="122" lengthAdjust="spacingAndGlyphs">OUR</text>
  <rect x="194" y="314" width="122" height="4" fill="var(--red)"/>
  <text class="title" x="328" y="343" font-size="96" textLength="492" lengthAdjust="spacingAndGlyphs">LEARNERS</text>

  <!-- pills -->
  <path class="pill" d="M372 433 H139 A86 86 0 0 0 139 605 H372"/>
  <path class="pill" d="M618 572 H849 A86 86 0 0 1 849 744 H618"/>
  <path class="pill" d="M372 711 H139 A86 86 0 0 0 139 883 H372"/>
  <path class="pill" d="M618 849 H849 A86 86 0 0 1 849 1021 H618"/>

  <!-- connecting chain -->
  <path class="chain" d="M373 520 C470 520 520 657 615 657 C520 657 470 797 373 797 C470 797 520 935 615 935"/>
  <circle class="node-ring" cx="373" cy="520" r="76"/>
  <circle class="node-ring" cx="615" cy="657" r="76"/>
  <circle class="node-ring" cx="373" cy="797" r="76"/>
  <circle class="node-ring" cx="615" cy="935" r="76"/>
  <circle class="node-disc" cx="373" cy="520" r="66"/>
  <circle class="node-disc" cx="615" cy="657" r="66"/>
  <circle class="node-disc" cx="373" cy="797" r="66"/>
  <circle class="node-disc" cx="615" cy="935" r="66"/>

  <!-- flow arrows -->
  <path class="flow-arrow" d="M468 572 L520 602 M506 602 L520 602 L514 590"/>
  <path class="flow-arrow" d="M520 712 L468 742 M474 730 L468 742 L482 742"/>
  <path class="flow-arrow" d="M468 850 L520 880 M506 880 L520 880 L514 868"/>

  <!-- icon: flame -->
  <path fill="var(--red-deep)" d="M372 486 C392 506 398 520 396 538 C394 552 384 562 372 562 C358 562 346 552 346 536 C346 522 356 514 362 502 C366 510 368 514 372 516 C374 506 374 496 372 486 Z"/>
  <path fill="var(--red)" d="M372 528 C380 538 384 546 382 552 C380 558 376 561 372 561 C366 561 362 556 362 550 C362 542 368 538 372 528 Z"/>

  <!-- icon: mountain -->
  <ellipse cx="594" cy="612" rx="13" ry="8" fill="#cfe3f2"/>
  <path fill="#4a3b36" d="M576 676 L598 634 L620 676 Z"/>
  <path fill="#a8584c" d="M604 676 L624 618 L650 676 Z"/>
  <path fill="#dde8f1" d="M624 618 L618 636 L630 636 Z"/>
  <rect x="575" y="674" width="77" height="4" rx="2" fill="#7cb342"/>

  <!-- icon: target -->
  <circle cx="372" cy="800" r="32" fill="var(--teal)"/>
  <circle cx="372" cy="800" r="23" fill="var(--paper)"/>
  <circle cx="372" cy="800" r="15" fill="#1f7f8c"/>
  <circle cx="372" cy="800" r="7" fill="var(--paper)"/>
  <path d="M372 800 L404 766" stroke="#7a7a7a" stroke-width="3"/>
  <path fill="#f47c7c" d="M398 760 L410 756 L414 768 L406 772 Z"/>

  <!-- icon: cloud with ladder -->
  <path fill="none" stroke="var(--sky)" stroke-width="3.5" d="M602 952 H596 C586 952 582 944 584 938 C586 930 592 926 600 928 C602 914 614 906 626 910 C634 912 638 920 638 926 C646 926 650 934 648 942 C646 948 640 952 634 952 H628"/>
  <path fill="none" stroke="var(--sky)" stroke-width="3.5" d="M607 932 V970 M623 932 V970 M607 944 H623 M607 956 H623 M607 966 H623"/>

  <!-- AGILITY -->
  <text class="label-lead" x="105" y="497" textLength="95" lengthAdjust="spacingAndGlyphs">LEARNERS WITH</text>
  <text class="label-key" x="209" y="497" textLength="79" lengthAdjust="spacingAndGlyphs">AGILITY</text>
  <text class="label-desc" x="68" y="520" textLength="220" lengthAdjust="spacingAndGlyphs">ARE DETERMINED, EQUIPPED</text>
  <text class="label-desc" x="79" y="540" textLength="209" lengthAdjust="spacingAndGlyphs">AND ABLE TO ACCOMPLISH</text>
  <text class="label-desc" x="176" y="560" textLength="112" lengthAdjust="spacingAndGlyphs">GREAT THINGS</text>

  <!-- ALTITUDE -->
  <text class="label-lead" x="708" y="622" textLength="96" lengthAdjust="spacingAndGlyphs">LEARNERS WITH</text>
  <text class="label-key" x="810" y="622" textLength="101" lengthAdjust="spacingAndGlyphs">ALTITUDE</text>
  <text class="label-desc" x="704" y="648" textLength="184" lengthAdjust="spacingAndGlyphs">ACHIEVE GREAT THINGS</text>
  <text class="label-desc" x="704" y="668" textLength="190" lengthAdjust="spacingAndGlyphs">AND WORK TO ELEVATE</text>
  <text class="label-desc" x="704" y="688" textLength="60" lengthAdjust="spacingAndGlyphs">OTHERS</text>

  <!-- ASPIRATION -->
  <text class="label-lead" x="66" y="770" textLength="95" lengthAdjust="spacingAndGlyphs">LEARNERS WITH</text>
  <text class="label-key" x="167" y="770" textLength="126" lengthAdjust="spacingAndGlyphs">ASPIRATION</text>
  <text class="label-desc" x="98" y="796" textLength="194" lengthAdjust="spacingAndGlyphs">INSPIRED AND BELIEVE IN</text>
  <text class="label-desc" x="98" y="816" textLength="194" lengthAdjust="spacingAndGlyphs">PURSUING GREAT THINGS</text>

  <!-- AGENCY -->
  <text class="label-lead" x="710" y="907" textLength="95" lengthAdjust="spacingAndGlyphs">LEARNERS WITH</text>
  <text class="label-key" x="812" y="907" textLength="87" lengthAdjust="spacingAndGlyphs">AGENCY</text>
  <text class="label-desc" x="708" y="933" textLength="212" lengthAdjust="spacingAndGlyphs">BELIEVE IN THEIR CAPACITY</text>
  <text class="label-desc" x="708" y="953" textLength="214" lengthAdjust="spacingAndGlyphs">AND RESPONSIBILITY TO DO</text>
  <text class="label-desc" x="708" y="973" textLength="116" lengthAdjust="spacingAndGlyphs">GREAT THINGS.</text>

  <!-- school marks -->
  <circle cx="134" cy="1306" r="33" fill="var(--red-deep)"/>
  <text class="school-name" x="174" y="1306" textLength="266" lengthAdjust="spacingAndGlyphs">Bayview Private School</text>
  <text class="school-tag" x="174" y="1328" textLength="266" lengthAdjust="spacingAndGlyphs">Where every child is special</text>

  <circle cx="735" cy="1306" r="34" fill="var(--red-deep)"/>
  <text class="school-name-alt" x="776" y="1294" font-size="21" textLength="118" lengthAdjust="spacingAndGlyphs">BAYVIEW</text>
  <text class="school-name-alt" x="776" y="1314" font-size="15" textLength="118" lengthAdjust="spacingAndGlyphs">COMMUNITY</text>
  <text class="school-name-alt" x="776" y="1334" font-size="15" textLength="76" lengthAdjust="spacingAndGlyphs">SCHOOL</text>
</svg>
</body>
</html>
```